Mail - Scan, Sort & Forward - Web Design

We need a web design for a mail scan, store, view and forward service. It is a lifestyle service predicated on freedom, convenience, ease of access, ease of use, security, safety. It involves personal information and is accessed remotely.
No branding or style guide is yet complete so an open pallet is available but design should convey simplicity as it targets demographic 45-75 years travellers but also high net worth multi location professionals, miners and other multi-location workers.
Competitor sites are: (for business description examples)
www.quellarbox.example
www.trimbeldesk.example.au
www.norvandelsupply.example.au
Updates

Attached files are wireframes which show how the service will work (UI). You should use these to form ideas about your web design for the service. They are not templates nor am I looking for a UI dev (yet).

Target Market(s)

Travellers ( especially retirees) and multi-location workers eg miners

Industry/Entity Type

Business

Requirements
Must have
• Being a lifestyle site, the pages must be low on text, lite layout, imagery addressing the target market.
Navigation should be simple to use
Concept of visitor / member / client should be addressed. The user needs to be able to permission other user groups (read-only)
Talk to reasons why prospects want to use this service.
Nice to have
• access to view nearest Kelm Rout office.
Regular call to action like survey, quiz or did you know info which may keep the user returning to the site.
Campaign section which enables customising of campaigns on an ongoing basis
Ability to access and download Terms & conditions, brochures .pdf or other information.
Simulate how service works..video or webcast
Should not have
• Do not want heavy or dense text everywhere. Use imagery where possible. Icons should be thematic not isolated.

```html
<!DOCTYPE html>
<html lang="en">
<head>
<meta charset="utf-8">
<title>Online Mail Service</title>
<link href="https://fonts.googleapis.com/css2?family=Open+Sans:wght@400;600;700&display=swap" rel="stylesheet">
<style>
:root{
  --page-bg:#ffffff;
  --outer-bg:#ffffff;
  --frame:#cfcfcf;
  --ink:#5d5d5d;
  --ink-dark:#3a3a3a;
  --ink-soft:#6f6f6f;
  --blue:#0a67a8;
  --blue-light:#1f8fd6;
  --blue-deep:#0b4f8d;
  --band:#eeeded;
  --panel-border:#dcdcdc;
  --panel-bg:#fbfbfb;
  --chip:#e6f3fb;
  --photo-a:#d9dadc;
  --photo-b:#b9bcc1;
}
*{box-sizing:border-box;margin:0;padding:0}
html,body{width:977px;height:1200px;overflow:hidden;background:var(--outer-bg)}
body{font-family:"Open Sans",Arial,sans-serif;color:var(--ink);position:relative}
.page{position:absolute;left:17px;top:23px;width:940px;height:1153px;border:1px solid var(--frame);background:var(--page-bg)}
.abs{position:absolute}

/* top utility bar */
.flag{left:538px;top:46px;width:25px;height:17px;background:linear-gradient(#2c4a8f,#1d3a7a);border:1px solid #c8c8c8}
.lang{left:584px;top:42px;width:157px;height:23px;border:1px solid #cfcfcf;border-radius:2px;font-size:10px;color:#777;padding:4px 9px;background:#fff}
.lang .caret{position:absolute;right:0;top:0;width:20px;height:21px;border-left:1px solid #ddd;display:flex;align-items:center;justify-content:center}
.util-btn{top:42px;width:54px;height:21px;border:1px solid #9cc8e2;background:linear-gradient(#f3fafe,#d9edf8);border-radius:2px;font-size:10px;font-weight:600;color:var(--blue-deep);text-align:center;line-height:19px}
.login{left:768px}.signup{left:831px}

/* brand */
.brand-art{left:58px;top:58px;width:70px;height:132px;background:linear-gradient(160deg,#ececec,#d8d8d8);border-radius:4px}
.brand-name{left:123px;top:96px;font-size:46px;font-weight:700;color:#5f5f5f;letter-spacing:-1.5px;line-height:1}
.brand-tag{left:125px;top:149px;font-size:13.5px;color:#777;letter-spacing:-.3px}

/* main nav */
.nav{left:421px;top:121px;height:32px;display:flex;gap:6px}
.nav a{display:block;height:32px;line-height:32px;padding:0;text-align:center;color:#fff;font-size:13px;font-weight:700;text-decoration:none;background:linear-gradient(var(--blue-light),var(--blue-deep));border-bottom:3px solid #07406f}
.nav .home{width:35px}.nav .about{width:86px}.nav .how{width:98px}.nav .pricing{width:87px}.nav .faq{width:42px}.nav .contact{width:86px}
.nav-rule{left:403px;top:159px;width:554px;height:1px;background:linear-gradient(90deg,transparent,#e2e2e2 20%)}

/* hero */
.hero-photo{left:126px;top:213px;width:311px;height:307px;background:linear-gradient(180deg,var(--photo-a),var(--photo-b));border-radius:6px 6px 0 0}
.hero-title{left:503px;top:255px;font-size:37px;font-weight:600;color:#5e5e5e;letter-spacing:-.5px;line-height:1.1}
.hero-sub{left:504px;top:296px;font-size:19px;color:#5e5e5e;line-height:1.1}
.hero-copy{left:504px;top:340px;width:400px;font-size:12.5px;line-height:23px;color:#555}
.btn{display:block;text-align:center;color:#fff;font-weight:700;background:linear-gradient(var(--blue-light),var(--blue-deep));border-radius:2px;box-shadow:0 1px 2px rgba(0,0,0,.3);text-decoration:none}
.hero-btn{left:503px;top:440px;width:124px;height:28px;line-height:28px;font-size:11px}

/* benefits band */
.band{left:18px;top:520px;width:938px;height:76px;background:var(--band);border-top:1px solid #e0e0e0;border-bottom:1px solid #dedede}
.benefit{top:544px}
.benefit h3{font-size:12px;font-weight:600;color:var(--ink-dark)}
.benefit p{font-size:10.5px;color:#666;margin-top:1px}
.b1{left:109px}.b2{left:277px}.b3{left:438px}.b4{left:594px}.b5{left:747px}

/* intro */
.intro{left:103px;top:633px;width:405px}
.intro h2{font-size:21px;font-weight:400;color:#555;letter-spacing:-.2px}
.intro p{font-size:12.5px;line-height:21.8px;color:#555;margin-top:6px}
.intro p+p{margin-top:8px}
.intro-btn{left:394px;top:851px;width:110px;height:30px;line-height:30px;font-size:12px}

/* side panels */
.panel{left:602px;width:282px;border:1px solid var(--panel-border);background:var(--panel-bg);border-radius:3px;box-shadow:0 1px 2px rgba(0,0,0,.08)}
.panel-head{font-size:13px;color:#4a4a4a;height:33px;line-height:33px;padding-left:28px;position:relative}
.panel-head svg{position:absolute;left:10px;top:12px}
.video-panel{top:633px;height:203px}
.video{position:absolute;left:32px;top:41px;width:222px;height:146px;background:#1d1d1d;border:1px solid #999}
.video .bar{position:absolute;left:0;bottom:0;width:100%;height:14px;background:#e1e1e1}
.acc1{top:853px}.acc2{top:901px}

/* promo */
.promo{left:603px;top:954px;width:281px;height:147px;background:linear-gradient(#1580cf,#0a4f94);text-align:center;color:#fff}
.promo .small{font-size:16px;font-weight:700;margin-top:24px;letter-spacing:-.3px}
.promo .big{font-size:44px;font-weight:700;line-height:1;margin-top:1px;letter-spacing:-.5px}
.promo-btn{position:absolute;left:67px;top:99px;width:146px;height:29px;line-height:29px;background:linear-gradient(#fafafa,#d6d6d6);border:1px solid #bbb;color:#888;font-size:13px;font-weight:700;border-radius:2px}

/* footer */
.social{left:109px;top:1075px;display:flex;gap:9px}
.social span{width:24px;height:24px;border-radius:50%;background:#eef3f7;border:1px solid #d7dee4;display:block}
.foot-links{top:1128px;font-size:11px;color:#777}
.foot-links span{margin:0 7px;color:#aaa}
.foot-left{left:103px}
.foot-right{right:103px;text-align:right}
</style>
</head>
<body>
<div class="page"></div>

<div class="abs flag" role="img" aria-label="English language flag"></div>
<div class="abs lang">Choose Language...
  <span class="caret"><svg width="7" height="10" viewBox="0 0 7 10"><path d="M0 4 3.5 0 7 4ZM0 6l3.5 4L7 6Z" fill="#888"/></svg></span>
</div>
<div class="abs util-btn login">Login</div>
<div class="abs util-btn signup">Sign Up</div>

<div class="abs brand-art" role="img" aria-label="Paper plane with dotted flight path"></div>
<div class="abs brand-name">Your Logo</div>
<div class="abs brand-tag">Keeping you intouch when your on the go!</div>

<nav class="abs nav">
  <a class="home" href="#" aria-label="Home"><svg width="14" height="13" viewBox="0 0 14 13" style="margin-top:9px"><path d="M7 0 0 6h2v7h4V9h2v4h4V6h2Z" fill="#fff"/></svg></a>
  <a class="about" href="#">About Us</a>
  <a class="how" href="#">How it works</a>
  <a class="pricing" href="#">Pricing</a>
  <a class="faq" href="#">FAQs</a>
  <a class="contact" href="#">Contact Us</a>
</nav>
<div class="abs nav-rule"></div>

<div class="abs hero-photo" role="img" aria-label="Smiling couple holding web and mail icons"></div>
<h1 class="abs hero-title">Online Mail Service</h1>
<div class="abs hero-sub">never get tied down by your mailbox again</div>
<p class="abs hero-copy">Get your mail and stay intouch, even if you travel or live overseas. Why wait? Get your important mail scanned and read it online within a day! So stay intouch when you plan on being away!</p>
<a class="abs btn hero-btn" href="#">Find Out More</a>

<div class="abs band"></div>
<div class="abs benefit b1"><h3>Ease of use</h3><p>Mail, scan, sort &amp; forward</p></div>
<div class="abs benefit b2"><h3>Ease of access</h3><p>Online mail access 24/7</p></div>
<div class="abs benefit b3"><h3>Freedom</h3><p>Live &amp; travel anywhere</p></div>
<div class="abs benefit b4"><h3>Piece of mind</h3><p>Protect your identity</p></div>
<div class="abs benefit b5"><h3>Security</h3><p>Securely store your mail</p></div>

<section class="abs intro">
  <h2>ONLINE MAIL SERVICE</h2>
  <p>A platform built to be simple convenient and reliable, with high security, 24/7 online mail access, you can have piece of mind you will be able to get your mail where ever and when ever!</p>
  <p>Our online mail service couldn't be easier! Get your documents scanned and read online with in a day, and be able to keep on top and manage your mail all by the click of a finger! View our video to find out more about our process!</p>
</section>
<a class="abs btn intro-btn" href="#">Find Out More</a>

<div class="abs panel video-panel">
  <div class="panel-head"><svg width="10" height="7" viewBox="0 0 10 7"><path d="M1 1l4 4 4-4" stroke="#1c6fb0" stroke-width="2" fill="none"/></svg>WATCH OUR VIDEO TO GET STARTED</div>
  <div class="video">
    <svg width="60" height="60" viewBox="0 0 60 60" style="position:absolute;left:81px;top:38px">
      <defs><radialGradient id="playGlow" cx="40%" cy="35%"><stop offset="0" stop-color="#8fc3ff"/><stop offset="1" stop-color="#1a5fd0"/></radialGradient></defs>
      <circle cx="30" cy="30" r="27" fill="url(#playGlow)" stroke="#e8e8e8" stroke-width="3"/>
      <path d="M23 17v26l21-13Z" fill="#fff"/>
    </svg>
    <div class="bar">
      <svg width="222" height="14" viewBox="0 0 222 14">
        <path d="M7 4v6l5-3Z" fill="#555"/>
        <rect x="18" y="6" width="110" height="2" fill="#999"/>
        <rect x="18" y="6" width="52" height="2" fill="#e04040"/>
        <circle cx="70" cy="7" r="3" fill="#777"/>
        <rect x="160" y="6" width="50" height="2" fill="#666"/>
      </svg>
    </div>
  </div>
</div>

<div class="abs panel acc1"><div class="panel-head"><svg width="7" height="10" viewBox="0 0 7 10"><path d="M1 1l4 4-4 4" stroke="#1c6fb0" stroke-width="2" fill="none"/></svg>FIND THE NEAREST KELM ROUT OFFICE</div></div>
<div class="abs panel acc2"><div class="panel-head"><svg width="7" height="10" viewBox="0 0 7 10"><path d="M1 1l4 4-4 4" stroke="#1c6fb0" stroke-width="2" fill="none"/></svg>JUST FOR FUN, QUESTIONNAIRE!</div></div>

<div class="abs promo">
  <div class="small">SIGN UP THIS MONTH AND GET</div>
  <div class="big">HALF PRICE</div>
  <div class="promo-btn">SIGN UP NOW!</div>
</div>

<div class="abs social" aria-label="Social links"><span></span><span></span><span></span></div>

<div class="abs foot-links foot-left">About Us<span>|</span>Tour<span>|</span>How It Works<span>|</span>Pricing<span>|</span>FAQs<span>|</span>Contact</div>
<div class="abs foot-links foot-right">Terms &amp; Conditions<span>|</span>Privacy<span>|</span>© 2011 Your Logo</div>
</body>
</html>
```